Industrial Consulting Firm Looking for a Responsive Design

Looking for a responsive design website of around 5 parent pages and about another 15 sub-pages for a small firm that works globally at industrial construction sites.

The web address http://torvexmilan.com/brightlo482917/index.html includes most of the content we would like to use for this effort. There are two deliverable options:

1) Use the provided design and create graphics for the website along with other requested tweaks.
2) Create a entirely new Layout/Design, which is original and different from this example, using content (text) from the provided link.

Content:

The main components of the website should include graphics for main page headers and picture links (along with the 7 main service sub pages), with industrial themes for the following pages:

Landing Page with clean presentation of our company and services.

Services: This main page has the most important sub-links in the website, the services which we want to highlight (Statistical Productivity Improvement, Veradin Process, Improving Project Performance, Work Process Analysis & Mapping, On-Site Training, and Facilitation Support). We would like to see graphic headers for each of these pages. Would like to have a fact sheet template.

News & Insight (Blog/Content Delivery format for press releases, latest news, publications, ability to be linked to company facebook feed a plus, etc)

Information about the company (Mission, Description, Company Profile, Clients Served,FAQs). Also, an interactive world map of past projects with capacity to update. It should work by obtaining a detail summary of past projects by hovering/clicking locations.

Contact Form including link to careers

Feel free to update any tables or content in pages. Ideas to highlight our services through graphics are appreciated.

Optional Features To Consider:

Client Testimonial Section (possibly on Main Page or About Us)
Filtering of News by Category/Date
Basic Site Search Functionality
Add a Registration option for Site Updates

Other Details:

If using pictures with people wearing safety gear: make sure that they are wearing safety glasses and a hard hat at a minimum and that the picture looks as realistic (environment-wise) as possible
Guidance on inclusion of other company logos in websites (as clients references, or displayed in pictures). Potentially looking to include them in website (either on landing page or clients served section in about us).

Important Considerations:

The design should be mobile (Android, IOS) friendly (NOT a separate mobile site)
The design should incorporate SEO.
The design should take security into account.
Coding required as well as graphic template files.

Upcoming Project Opportunity

Based on the demonstrated graphic design presented in this project, we might consider an additional project to expand on graphics package (including, but not limited to an info graphic).

Technical Requirements:

Languages Accepted: HTML, ASP.NET
To Run on a Server with: Windows IIS 7 or above
Restrictions: No languages requiring install on Windows IIS
Easily updated and maintained

Project will commit payment when we find at least one design our team agrees upon.

```html
<!DOCTYPE html>
<html lang="en">
<head>
<meta charset="utf-8">
<title>Halvaro Performance Resources</title>
<link href="https://fonts.googleapis.com/css2?family=Montserrat:wght@400;600;700&family=Open+Sans:wght@400;600;700&display=swap" rel="stylesheet">
<style>
:root{
  --navy:#0f3e6e;
  --navy-deep:#0b3460;
  --band:#124579;
  --band-dark:#0e3a68;
  --ink:#333;
  --muted:#777;
  --grey-bg:#e9edf1;
  --footer:#121212;
  --footer-bottom:#0a0a0a;
  --pin:#8fcf5c;
  --white:#fff;
}
*{margin:0;padding:0;box-sizing:border-box}
html,body{width:1200px;height:2281px;overflow:hidden}
body{font-family:"Open Sans",sans-serif;color:var(--ink);background:#fff;position:relative}
.abs{position:absolute}
h1,h2,h3,.mont{font-family:"Montserrat",sans-serif;font-weight:400}

/* header */
.site-header{left:0;top:0;width:1200px;height:91px;background:#fff;box-shadow:0 1px 4px rgba(0,0,0,.12);z-index:2}
.brand{left:111px;top:22px;display:flex;align-items:center;gap:10px}
.brand-dot{width:40px;height:40px;border-radius:50%;background:var(--navy)}
.brand-name{font-family:"Montserrat",sans-serif;font-weight:700;font-size:12.5px;line-height:14px;color:var(--navy);letter-spacing:.5px}
.main-nav{left:435px;top:29px;display:flex;height:38px;align-items:center;font-family:"Montserrat",sans-serif;font-size:12.5px;font-weight:600;color:#333}
.main-nav a{color:inherit;text-decoration:none;padding:0 20px;line-height:38px;white-space:nowrap}
.main-nav a.active{background:var(--navy);color:#fff;padding:0 18px}
.search-btn{left:1048px;top:29px;width:40px;height:38px;background:#999}

/* hero */
.hero{left:0;top:91px;width:1200px;height:519px;background:linear-gradient(180deg,#c4d8e6 0%,#a9c3d7 45%,#6f8fad 75%,#3f5f82 100%)}
.hero-title-box{left:259px;top:271px;width:684px;height:83px;background:rgba(255,255,255,.28);display:flex;align-items:center;justify-content:center}
.hero-title{font-size:35px;color:#2b3a4a;letter-spacing:1px}
.hero-sub{left:230px;top:374px;width:740px;text-align:center;font-family:"Montserrat",sans-serif;font-size:21px;line-height:31px;color:#3c4c5c}
.plus{border-radius:50%;background:var(--navy);color:#fff;display:flex;align-items:center;justify-content:center;font-weight:700}
.hero-arrow{top:332px;width:33px;height:33px;border-radius:50%;border:2px solid rgba(255,255,255,.7)}

/* welcome */
.welcome-title{left:0;top:648px;width:1200px;text-align:center;font-size:26px;color:#555}
.welcome-title strong,.section-title strong{color:var(--navy);font-weight:600}
.welcome-text{left:118px;top:693px;width:966px;text-align:center;font-size:11.6px;line-height:25px;color:#555}
.section-title{font-size:26px;color:#555}

/* services */
.services-band{left:0;top:841px;width:1200px;height:245px;background:var(--navy)}
.service-card{top:841px;width:245px;height:245px;color:#fff;text-align:center}
.service-card h3{position:absolute;left:6px;right:6px;bottom:150px;font-size:13.5px;font-weight:600;line-height:20px}
.service-card p{position:absolute;left:12px;right:12px;top:108px;font-size:10.6px;line-height:19px}
.service-card .plus{position:absolute;left:114px;top:209px;width:17px;height:17px;background:#fff;color:var(--navy);font-size:14px}
.service-card.active{background:#fff}
.service-card.active .card-head{position:absolute;left:0;top:0;width:245px;height:96px;background:#2f5f8f}
.service-card.active .card-head h3{bottom:8px}
.service-card.active p{color:#888}
.service-card.active .plus{background:var(--navy);color:#fff}
.band-arrow{top:942px}

/* news */
.news-title{left:111px;top:1122px}
.dot{top:1135px;width:9px;height:9px;border-radius:50%;background:#ccc}
.news-photo{left:111px;top:1177px;width:342px;height:196px;background:linear-gradient(135deg,#c9b48f 0%,#8c8f96 45%,#3f5b7e 100%);border:1px solid #ddd}
.news-date{left:473px;top:1178px;font-size:10.5px;font-weight:700;color:var(--navy)}
.news-head{left:473px;top:1198px;width:615px;font-size:14.5px;line-height:21px;color:#333}
.news-rule{left:473px;top:1247px;width:615px;height:1px;background:#ddd}
.news-body{left:473px;top:1256px;width:615px;font-size:11.4px;line-height:24px;color:#777}
.read-more{left:473px;top:1358px;font-size:12px;font-weight:700;color:var(--navy);letter-spacing:.3px}
.partners{left:105px;top:1420px;width:1000px;display:flex;justify-content:space-between;align-items:center}
.partner{height:30px;background:#cfcfcf;border-radius:3px}

/* location */
.location{left:0;top:1486px;width:1200px;height:345px;background:var(--band)}
.loc-title{left:111px;top:1508px;font-size:25px;color:#fff;font-weight:600}
.loc-select{left:110px;top:1560px;width:264px;height:54px;background:var(--band-dark);color:#fff;font-size:12.5px;padding:0 20px;display:flex;justify-content:space-between;align-items:center}
.loc-address{left:110px;top:1621px;width:264px;height:151px;background:var(--band-dark);color:#fff;font-size:11.5px;line-height:21px;padding:20px}
.world-map{left:441px;top:1491px;width:654px;height:327px;background:radial-gradient(ellipse at 50% 45%,#3c689a 0%,#2a5888 55%,rgba(18,69,121,0) 80%)}

/* mail */
.mail{left:0;top:1831px;width:1200px;height:235px;background:var(--grey-bg)}
.mail-title{left:111px;top:1853px;font-size:25px;color:#555}
.mail-sub{left:111px;top:1888px;font-size:9.5px;color:#888;letter-spacing:.5px}
.mail-rule{left:111px;top:1909px;width:475px;height:1px;background:#ccc}
.field{background:#fff;border:1px solid #ccc;font-size:11.5px;color:#888;padding:0 16px;display:flex;align-items:center}
.field.message{align-items:flex-start;padding-top:10px}
.send-btn{left:946px;top:1987px;width:142px;height:51px;background:var(--navy-deep);color:#fff;font-family:"Montserrat",sans-serif;font-weight:600;font-size:15px;display:flex;align-items:center;justify-content:center}

/* footer */
.footer{left:0;top:2066px;width:1200px;height:144px;background:var(--footer);color:#fff}
.foot-h{top:2092px;font-family:"Montserrat",sans-serif;font-weight:600;font-size:14.5px;color:#fff}
.foot-text{font-size:11px;line-height:20px;color:#999}
.news-input{left:563px;top:2130px;width:195px;height:40px;background:#fff;font-size:10.5px;color:#999;padding:0 14px;display:flex;align-items:center}
.sub-btn{left:758px;top:2130px;width:114px;height:40px;background:var(--navy-deep);color:#fff;font-size:10.5px;font-weight:700;display:flex;align-items:center;justify-content:center}
.social{top:2132px;width:36px;height:36px;background:#3b67a8}
.footer-bottom{left:0;top:2210px;width:1200px;height:71px;background:var(--footer-bottom);color:#ccc;font-size:10.5px}
</style>
</head>
<body>

<header class="abs site-header">
  <div class="abs brand"><span class="brand-dot"></span><span class="brand-name">HALVARO<br>PERFORMANCE<br>RESOURCES, INC.</span></div>
  <nav class="abs main-nav">
    <a class="active">HOME</a><a>SERVICES</a><a>NEWS &amp; INSIGHTS</a><a>ABOUT US</a><a>CONTACT</a><a>LOGIN</a>
  </nav>
  <div class="abs search-btn">
    <svg width="40" height="38" viewBox="0 0 40 38"><circle cx="19" cy="18" r="4.5" fill="none" stroke="#fff" stroke-width="2"/><line x1="22.5" y1="21.5" x2="25" y2="24" stroke="#fff" stroke-width="2"/></svg>
  </div>
</header>

<section class="abs hero" role="img" aria-label="Hazy city skyline under a pale blue sky"></section>
<div class="abs hero-title-box"><h1 class="hero-title">GLOBAL EXPERIENCE</h1></div>
<p class="abs hero-sub">HPR has partnered with clients on their most critical projects around the world.</p>
<div class="abs plus" style="left:590px;top:457px;width:22px;height:22px;font-size:18px">+</div>
<svg class="abs hero-arrow" style="left:24px" viewBox="0 0 33 33"><path d="M19 10 L12 16.5 L19 23 Z" fill="rgba(255,255,255,.8)"/></svg>
<svg class="abs hero-arrow" style="left:1139px" viewBox="0 0 33 33"><path d="M14 10 L21 16.5 L14 23 Z" fill="rgba(255,255,255,.8)"/></svg>

<h2 class="abs welcome-title">WELCOME TO <strong>HALVARO PERFORMANCE RESOURCES, INC</strong></h2>
<p class="abs welcome-text">Ut wisi enim ad minim veniam, quis nostrud exerci tation ullamcorper suscipit lobortis nisl ut aliquip ex ea commodo consequat. Duis autem vel eum iriure dolor in hendrerit in vulputate velit esse molestie consequat, vel illum dolore eu feugiat nulla facilisis at vero eros et accumsan et iusto odio dignissim qui blandit praesent luptatum zzril delenit augue duis dolore te feugait nulla facilisi.</p>

<h2 class="abs section-title" style="left:0;top:794px;width:1200px;text-align:center">OUR <strong>SERVICES</strong></h2>

<section class="abs services-band" role="img" aria-label="Industrial work photos tinted navy behind the service cards"></section>
<svg class="abs band-arrow" style="left:28px" width="34" height="60" viewBox="0 0 34 60"><path d="M30 2 L4 30 L30 58" fill="none" stroke="#fff" stroke-width="1.5"/></svg>
<svg class="abs band-arrow" style="left:1136px" width="34" height="60" viewBox="0 0 34 60"><path d="M4 2 L30 30 L4 58" fill="none" stroke="#fff" stroke-width="1.5"/></svg>

<article class="abs service-card" style="left:111px;background:#2a5a8a">
  <h3>STATISTICAL PRODUCTIVITY IMPROVEMENT</h3>
  <p>Lorem ipsum dolor sit amet, consectetuer adipiscing elit, sed diam nonummy nibh euismod tincidunt ut laoreet dolore magna aliquam erat volutpat.</p>
  <span class="plus">+</span>
</article>
<article class="abs service-card" style="left:356px;background:#3a6591">
  <h3>VERADIN PROCESS</h3>
  <p>Lorem ipsum dolor sit amet, consectetuer adipiscing elit, sed diam nonummy nibh euismod tincidunt ut laoreet dolore magna aliquam erat volutpat.</p>
  <span class="plus">+</span>
</article>
<article class="abs service-card active" style="left:599px">
  <div class="card-head"><h3>IMPROVING PROJECT PERFORMANCE</h3></div>
  <p>Lorem ipsum dolor sit amet, consectetuer adipiscing elit, sed diam nonummy nibh euismod tincidunt ut laoreet dolore magna aliquam erat volutpat.</p>
  <span class="plus">+</span>
</article>
<article class="abs service-card" style="left:844px;background:#2d5b89">
  <h3>WORK PROCESS ANALYSIS &amp; MAPPING</h3>
  <p>Lorem ipsum dolor sit amet, consectetuer adipiscing elit, sed diam nonummy nibh euismod tincidunt ut laoreet dolore magna aliquam erat volutpat.</p>
  <span class="plus">+</span>
</article>

<h2 class="abs section-title news-title">NEWS &amp; <strong>INSIGHT</strong></h2>
<span class="abs dot" style="left:1046px"></span><span class="abs dot" style="left:1063px;background:#666"></span><span class="abs dot" style="left:1080px"></span>

<div class="abs news-photo" role="img" aria-label="Two engineers in hard hats reviewing plans on site"></div>
<p class="abs news-date">JANUARY 27, 2015</p>
<h3 class="abs news-head" style="font-family:'Open Sans',sans-serif">Lorem ipsum dolor sit amet, consectetuer adipiscing elit, sed diam nonummy nibh euismod tincidunt ut laoreet dolore magna aliquam erat volutpat</h3>
<div class="abs news-rule"></div>
<p class="abs news-body">Duis autem vel eum iriure dolor in hendrerit in vulputate velit esse molestie consequat, vel illum dolore eu feugiat nulla facilisis at vero eros et accumsan et iusto odio dignissim qui blandit praesent luptatum zzril delenit augue duis dolore te feugait nulla facilisi. Nam liber tempor cum soluta nobis eleifend option congue nihil imperdiet doming id quod mazim placerat facer possim assum. Typi non habent claritatem...</p>
<p class="abs read-more">READ MORE</p>

<div class="abs partners" aria-label="Client badges">
  <span class="partner" style="width:105px"></span>
  <span class="partner" style="width:88px"></span>
  <span class="partner" style="width:80px"></span>
  <span class="partner" style="width:128px"></span>
  <span class="partner" style="width:62px"></span>
  <span class="partner" style="width:140px"></span>
  <span class="partner" style="width:80px"></span>
</div>

<section class="abs location"></section>
<h2 class="abs loc-title">OUR LOCATION</h2>
<div class="abs loc-select"><span>USA</span><span style="font-size:10px">&#8964;</span></div>
<div class="abs loc-address">123 , Lorem Ipsm, Lorem Ipsm,<br>Lorem Ipsm, Lorem Ipsm,<br>USA - 123 456<br><br>Phone : 123 456 789 000</div>
<div class="abs world-map" role="img" aria-label="World map of past project locations"></div>

<svg class="abs" style="left:0;top:1486px" width="1200" height="345" viewBox="0 1486 1200 345">
  <defs>
    <g id="pin"><path d="M0 0 C-8 -8 -8 -20 0 -20 C8 -20 8 -8 0 0 Z" fill="var(--pin)"/><circle cx="0" cy="-13" r="3.5" fill="#fff"/></g>
  </defs>
  <use href="#pin" transform="translate(557 1620) scale(1.6)"/>
  <use href="#pin" transform="translate(600 1635)"/>
  <use href="#pin" transform="translate(847 1603)"/>
  <use href="#pin" transform="translate(983 1763)"/>
  <use href="#pin" transform="translate(1030 1763)"/>
  <text x="540" y="1573" fill="#fff" font-family="Montserrat,sans-serif" font-weight="700" font-size="14">USA</text>
  <text x="582" y="1607" fill="#fff" font-family="Open Sans,sans-serif" font-weight="700" font-size="8">ILLINOIS</text>
  <text x="798" y="1576" fill="#fff" font-family="Open Sans,sans-serif" font-weight="700" font-size="8">ATYRAU,KAZAKHSTAN</text>
  <text x="968" y="1734" fill="#fff" font-family="Open Sans,sans-serif" font-weight="700" font-size="8">PERTH</text>
  <text x="1005" y="1734" fill="#fff" font-family="Open Sans,sans-serif" font-weight="700" font-size="8">AUSTRALIA</text>
</svg>

<section class="abs mail"></section>
<h2 class="abs mail-title">SEND <strong style="color:var(--navy);font-weight:600">MAIL</strong></h2>
<p class="abs mail-sub">WRITE TO US</p>
<div class="abs mail-rule"></div>
<div class="abs field" style="left:111px;top:1935px;width:225px;height:45px">Name</div>
<div class="abs field" style="left:360px;top:1935px;width:226px;height:45px">Email Address</div>
<div class="abs field" style="left:111px;top:1995px;width:225px;height:45px">Phone</div>
<div class="abs field" style="left:360px;top:1995px;width:226px;height:45px">Company Name</div>
<div class="abs field message" style="left:611px;top:1935px;width:309px;height:105px">Message</div>
<div class="abs send-btn">SEND</div>

<footer class="abs footer"></footer>
<h3 class="abs foot-h" style="left:111px">CONTACT US</h3>
<svg class="abs" style="left:115px;top:2128px" width="9" height="13" viewBox="0 0 9 13"><path d="M4.5 13 C0 7 0 5 0 4.5 A4.5 4.5 0 0 1 9 4.5 C9 5 9 7 4.5 13Z" fill="#3b7bc8"/><circle cx="4.5" cy="4.5" r="1.6" fill="#121212"/></svg>
<p class="abs foot-text" style="left:133px;top:2124px">COMPANY NAME<br>P.O. Box 728, Dunmore,<br>NC 27401</p>
<svg class="abs" style="left:329px;top:2131px" width="14" height="10" viewBox="0 0 14 10"><rect width="14" height="10" rx="1" fill="#3b7bc8"/><path d="M0 0 L7 6 L14 0" fill="none" stroke="#121212" stroke-width="1.2"/></svg>
<svg class="abs" style="left:329px;top:2155px" width="13" height="13" viewBox="0 0 13 13"><rect width="13" height="13" rx="2" fill="#3b7bc8"/><path d="M4 3 L5.5 5 L4.8 6 C5.5 7.5 6.5 8.5 7.5 9 L8.5 8.3 L10 9.8 L9 10.8 C6 10.5 2.5 7 2.5 4 Z" fill="#121212"/></svg>
<p class="abs foot-text" style="left:354px;top:2126px">contact@halvaroresources.com</p>
<p class="abs foot-text" style="left:354px;top:2151px">+123.456.789</p>
<h3 class="abs foot-h" style="left:563px">NEWSLETTER SIGNUP</h3>
<div class="abs news-input">Email Address</div>
<div class="abs sub-btn">SUBSCRIBE</div>
<h3 class="abs foot-h" style="left:948px">CONNECT US</h3>
<span class="abs social" style="left:948px" aria-label="Social profile one"></span>
<span class="abs social" style="left:993px;background:#4d9bd6" aria-label="Social profile two"></span>

<div class="abs footer-bottom"></div>
<p class="abs" style="left:111px;top:2237px;font-size:10.5px;color:#fff">ABOUT US &nbsp;&nbsp;| &nbsp;&nbsp;FAQ &nbsp;&nbsp;| &nbsp;&nbsp;SERVICES</p>
<p class="abs" style="left:810px;top:2237px;width:278px;text-align:right;font-size:10.5px;color:#777">Copyright @ 2015 Company Name. All Right Reserved.</p>

</body>
</html>
```